Pull Up Banner - Recruitment Company

We would like a design for a pull up banner.

For context: we are a recruitment business. We specialise in helping people in healthcare industry to find jobs in Australia.

I have come up with several ideas and text for the banner. Feel free to use the following as you see appropriate:

- Our logo (see attached)
- 'Healthcare Recruitment Agency'
- Some sort of imagine / cartoon of medical professionals (ie. doctor, nurse, physiotherapist, speech pathologist). A cartoon is more friendly than committing to a photo
- 'Empowering your next career move'
- 'Discover tailored opportunities based on your career preferences'
- Dot points (allied health, nursing, medical imaging)
- Contact info at the bottom including our website (www.plimtaffing.com.au, our Instagram handle @plimtaffing, Mobile: XXXX XXX XXX. The title section for contact information could be 'Get in touch:'

Feel free to submit a couple of designs and we can merge aspects that look good on your designs and find the perfect fit.
Thank you
Updates

Hello,

Thank you for your initial submissions to this project. I appreciate the time you've invested.

After reviewing the first attempt, I'd like to share some feedback and initial observations:

- Professionalism and engagement: Is the overall appearance of the banner professional? It's crucial that we have a high-quality design as this will represent our business.

- Image selection: The image (whether cartoon or real people) appears quite generic. Please consider submitting the banner with a few different photos in the middle for us to choose from. Ensure the image is a good fit and not simply a generic stock photo.

- Contact section: Kindly remove the phone number; we no longer wish to include it on the banner. Instead, please include our website (www.plimtaffing.com.au) and Instagram handle (@plimtaffing).

- Color scheme: White, black, and red/pink are preferred, or alternatively, blue. However, please avoid incorporating too many different colors as it may detract from the professional appearance.

We will be printing the design on a banner and require it to look professional and engaging.

Thank you once again for your submissions. I hope the feedback provided above is helpful.

Warm regards,

Target Market(s)

Allied Health Australia

Font styles to use
Serif

Colors
0054AA
0677BA
7BADD7
CADEEF
E8F1F8
0094D4
00A9DD
6FCCEA
C7EBF8
E9F6FB
EB3D1F
EC4F4E
F09395
F8D3D4
FCEDEE

```html
<!DOCTYPE html>
<html lang="en">
<head>
<meta charset="utf-8">
<title>Plim Taffing – Healthcare Recruitment Agency</title>
<link rel="stylesheet" href="https://fonts.googleapis.com/css2?family=DM+Serif+Display:ital@0;1&family=Montserrat:wght@400;500;600;800&display=swap">
<style>
  :root {
    --bg-light: #ececf0;
    --bg-tint: #d9dbeb;
    --ink: #1c1b24;
    --brand: #3c4796;
    --brand-deep: #2e2a80;
    --accent: #8ff0f0;
    --ghost: #d6d8e2;
    --white: #ffffff;
  }
  * { margin: 0; padding: 0; box-sizing: border-box; }
  html, body { width: 675px; height: 1200px; overflow: hidden; }
  body { font-family: "Montserrat", Arial, sans-serif; color: var(--ink); }

  .banner {
    position: relative;
    width: 675px;
    height: 1200px;
    overflow: hidden;
    background: radial-gradient(circle at 100% 0%, var(--bg-tint) 0%, var(--bg-light) 45%);
  }
  .decor { position: absolute; inset: 0; width: 675px; height: 1200px; }

  .brand-name {
    position: absolute;
    left: 56px; top: 66px;
    font-weight: 800;
    font-size: 34px;
    letter-spacing: 2px;
    color: var(--ink);
  }

  .headline {
    position: absolute;
    left: 54px; top: 238px;
    font-family: "DM Serif Display", Georgia, serif;
    font-weight: 400;
    color: var(--ink);
    line-height: 1;
  }
  .headline .line-small { display: block; font-size: 51px; }
  .headline .line-large { display: block; font-size: 64px; margin-top: 6px; }

  .tagline {
    position: absolute;
    left: 55px; top: 374px;
    font-family: "DM Serif Display", Georgia, serif;
    font-style: italic;
    font-size: 28px;
    color: var(--ink);
  }
  .tagline-rule {
    position: absolute;
    left: 52px; top: 416px;
    width: 315px; height: 2px;
    background: var(--brand-deep);
  }

  .intro { position: absolute; left: 55px; top: 468px; }
  .intro-title { font-weight: 500; font-size: 24.5px; }
  .intro-sub { font-weight: 500; font-size: 18px; margin-top: 6px; }

  .specialties { position: absolute; left: 0; top: 562px; list-style: none; }
  .specialty {
    width: 280px; height: 54px;
    margin-bottom: 29px;
    background: var(--brand);
    border: 2px solid var(--brand-deep);
    border-left: none;
    border-radius: 0 27px 27px 0;
    color: var(--white);
    font-weight: 500;
    font-size: 21px;
    padding-left: 54px;
    line-height: 50px;
  }

  .footer-band {
    position: absolute;
    left: 0; top: 1097px;
    width: 675px; height: 103px;
    background: var(--brand);
  }
  .contact {
    position: absolute;
    left: 54px; top: 1122px;
    color: var(--white);
    font-size: 15px;
    line-height: 21px;
    font-weight: 400;
  }

  .portrait {
    position: absolute;
    left: 300px; top: 603px;
    width: 375px; height: 597px;
    border-radius: 190px 190px 0 0;
    background: linear-gradient(180deg, #e9eaf0 0%, #f5f6fa 40%, #dfe6f3 100%);
  }
  .stethoscope-mark {
    position: absolute;
    left: 58px; top: 815px;
    width: 160px; height: 160px;
    border-radius: 50%;
    background: var(--ghost);
    opacity: 0.45;
  }
</style>
</head>
<body>
<main class="banner">
  <svg class="decor" viewBox="0 0 675 1200" aria-hidden="true">
    <!-- plus shapes -->
    <g fill="var(--ghost)">
      <rect x="101" y="174" width="83" height="30"/>
      <rect x="128" y="148" width="29" height="82"/>
      <rect x="462" y="454" width="126" height="45"/>
      <rect x="503" y="412" width="45" height="127"/>
    </g>
    <!-- top right orbit lines -->
    <g fill="none" stroke="var(--brand-deep)" stroke-width="2">
      <ellipse cx="520" cy="90" rx="170" ry="55" transform="rotate(-42 520 90)"/>
      <ellipse cx="545" cy="80" rx="200" ry="62" transform="rotate(-38 545 80)"/>
    </g>
    <circle cx="562" cy="150" r="15" fill="var(--accent)"/>
    <!-- lower arcs -->
    <circle cx="631" cy="1188" r="397" fill="var(--brand)"/>
    <circle cx="628" cy="1181" r="421" fill="none" stroke="var(--brand-deep)" stroke-width="2"/>
    <circle cx="229" cy="959" r="15" fill="var(--accent)"/>
  </svg>

  <div class="stethoscope-mark" role="img" aria-label="Faint stethoscope decoration"></div>

  <div class="brand-name">PLIM TAFFING</div>

  <h1 class="headline">
    <span class="line-small">Healthcare</span>
    <span class="line-large">Recruitment Agency</span>
  </h1>
  <p class="tagline">Empowering your next career move</p>
  <div class="tagline-rule"></div>

  <div class="intro">
    <p class="intro-title">Discover Tailored Opportunities</p>
    <p class="intro-sub">Based on your Career Preferences</p>
  </div>

  <ul class="specialties">
    <li class="specialty">Allied Health</li>
    <li class="specialty">Nursing</li>
    <li class="specialty">Medical Imaging</li>
  </ul>

  <div class="footer-band"></div>
  <div class="portrait" role="img" aria-label="Healthcare professional in white coat with mask, gloves, stethoscope and tablet"></div>

  <div class="contact">
    <p>Instagram - @plimtaffing</p>
    <p>www.plimtaffing.com.au</p>
  </div>
</main>
</body>
</html>
```